Apricot Variety Sheet - Meadowlark Orchard Co

We are needing a variety sheet that we can hand out that will describe the different apricot vatieties we have available. The attached document has the name of the variety along with a description that will need to be on the sheet. We are looking for a modern, appealing way to display this information on 1 page (if needed, it can be front and back)
Updates

Apologies for the delay; we are overwhelmed with the great design options and will be sorting through them all (across our contests) to pick a collective. Thank you for your patience.

Target Market(s)

Growers and consumers

Industry/Entity Type

Agriculture

Requirements
Must have
• Easy to read
• Natural color palettes to emphasize the agricultural nature
• Clearly show washington as the origin in the title or at the top
Nice to have
• incorporate Apricots in the design

```html
<!DOCTYPE html>
<html lang="en">
<head>
<meta charset="utf-8">
<title>Apricot Variety Sheet – Meadowlark Orchard Co</title>
<link rel="stylesheet" href="https://fonts.googleapis.com/css2?family=Montserrat:wght@600;800&family=Oswald:wght@600&family=Lato:wght@400;700&display=swap">
<style>
  :root {
    --leaf-pale: #eef6c8;
    --leaf-light: #cfeaa0;
    --leaf-mid: #9fd979;
    --leaf-deep: #5fbf62;
    --brand-green: #1f6a45;
    --ribbon-red: #c8141a;
    --title-red: #c8141a;
    --label-gold: #f6e27a;
    --ink: #1d2a1a;
    --band: rgba(255, 255, 240, 0.45);
    --fruit: #e0603a;
  }
  * { margin: 0; padding: 0; box-sizing: border-box; }
  html, body { width: 1068px; height: 1200px; overflow: hidden; background: #f2f2f2; }
  .sheet {
    position: relative;
    width: 1068px;
    height: 1200px;
    overflow: hidden;
    background:
      radial-gradient(ellipse 420px 300px at 20% 8%, rgba(255,255,230,0.7), transparent 70%),
      radial-gradient(ellipse 500px 260px at 80% 84%, rgba(230,250,150,0.55), transparent 70%),
      linear-gradient(180deg, var(--leaf-light) 0%, var(--leaf-pale) 22%, var(--leaf-pale) 45%, var(--leaf-mid) 75%, var(--leaf-deep) 92%, var(--leaf-mid) 100%);
    border-bottom: 3px solid var(--ribbon-red);
    font-family: 'Lato', sans-serif;
  }
  .masthead { position: absolute; left: 222px; top: 30px; display: flex; align-items: center; gap: 36px; }
  .masthead .mark {
    width: 170px; height: 124px; border-radius: 50%;
    background: radial-gradient(circle at 40% 40%, #f38a5a, var(--fruit) 60%, #b8402a);
  }
  .masthead .brand-name {
    font-family: 'Montserrat', sans-serif; font-weight: 800;
    font-size: 34px; line-height: 1.1; color: var(--brand-green);
  }
  .sheet-title {
    position: absolute; left: 0; right: 0; top: 162px;
    display: flex; align-items: center; justify-content: center; gap: 14px;
    font-family: 'Montserrat', sans-serif; font-weight: 600;
    font-size: 46px; color: var(--title-red);
  }
  .sheet-title::before, .sheet-title::after {
    content: ""; width: 110px; height: 2px; background: var(--title-red);
  }
  .varieties { position: absolute; left: 0; right: 0; top: 240px; list-style: none; }
  .variety { position: relative; height: 78px; }
  .variety::before {
    content: ""; position: absolute; left: 0; right: 0; top: 6px; height: 60px;
    background: linear-gradient(90deg, transparent, var(--band) 40%, var(--band) 80%, transparent);
  }
  .variety-name {
    position: absolute; left: 0; top: 8px; width: 271px; height: 54px;
    background: var(--ribbon-red);
    clip-path: polygon(0 0, 100% 0, 88% 50%, 100% 100%, 0 100%);
    font-family: 'Oswald', sans-serif; font-weight: 600; font-size: 28px;
    color: var(--label-gold); line-height: 54px; padding-left: 36px;
  }
  .variety-text {
    position: absolute; left: 288px; top: 4px; width: 738px;
    font-size: 17px; line-height: 20px; color: var(--ink); font-weight: 700;
  }
</style>
</head>
<body>
<main class="sheet">
  <header class="masthead">
    <div class="mark" role="img" aria-label="Apricot fruit"></div>
    <div class="brand-name">Washington State<br>Meadowlark Orchard Co</div>
  </header>
  <h1 class="sheet-title">Apricot Variety Sheet</h1>
  <ul class="varieties">
    <li class="variety"><span class="variety-name">RIVAL :</span><p class="variety-text">Great flavor with a fine, firm texture distinguishes this large oval-shaped apricot. The skin is light orange with a red blush. The flesh is a lush deep orange color. Available early July- early August.</p></li>
    <li class="variety"><span class="variety-name">Robada :</span><p class="variety-text">This jumbo apricot has a delicious floral flavor with a firm texture. Bright orange, with a deep red blush over nearly half its surface. Available early June</p></li>
    <li class="variety"><span class="variety-name">Perfection :</span><p class="variety-text">This classic large oval apricot is deep orange with an oblong shape and firm texture. The flesh is a yellow/orange color that is very sweet and full of flavor. Available mid July - mid August.</p></li>
    <li class="variety"><span class="variety-name">Patterson :</span><p class="variety-text">This apricot has a well-balanced flavor and an excellent shelf life. This is perfect for canning or drying. It has streaked red over yellow skin, with a firm flesh. Available mid – late June.</p></li>
    <li class="variety"><span class="variety-name">Tomcot :</span><p class="variety-text">Tangy, sweet flavor with a firm texture. This oval apricot is light orange with a slight blush color. The flesh is a dark orange. Available late June – late July.</p></li>
    <li class="variety"><span class="variety-name">Goldrich :</span><p class="variety-text">This apricot is round with a bright orange skin color and a deep orange flesh. It has a mild, sweet flavor with a firm texture. Available early July – mid August.</p></li>
    <li class="variety"><span class="variety-name">Casselbrite :</span><p class="variety-text">This medium sized apricot is golden orange with a slight red blush. It has a mild sweet-tart flavor that is good for eating out of hand. Available late June- early July.</p></li>
    <li class="variety"><span class="variety-name">Goldbar :</span><p class="variety-text">Moderately juicy, this large oval-shaped apricot has a light yellow-orange with a reddish blush. The flesh is firm, meaty, and has a light orange color. Available late June – end of July.</p></li>
    <li class="variety"><span class="variety-name">Sweet Juillet :</span><p class="variety-text">This special variety has a unique, sweet flavor with a juicy flesh. It is bright orange in color with a bright orange flesh. Available through July.</p></li>
    <li class="variety"><span class="variety-name">Tasty Rich :</span><p class="variety-text">This early variety is light yellow-orange colored with a firm texture. Very juicy with an enticing flavor. Available through June.</p></li>
    <li class="variety"><span class="variety-name">Goldstrike :</span><p class="variety-text">A larger apricot with light orange, blushed skin. Firm texture with a slight tart taste until fully ripened, then very sweet. Available mid June - mid July.</p></li>
    <li class="variety"><span class="variety-name">Riland :</span><p class="variety-text">Very aromatic and sweet, this apricot is orange with a red blush. It has a yellow-orange colored flesh and a round shape. Available mid-June to end of July.</p></li>
  </ul>
</main>
</body>
</html>
```